Profesional personal website needs design and business card

I need a business card with my professional name as a logo "Orlan Vitality" for my business. I am a Wellness Coach, consultant and trainer. So it should be professional, wellness oriented and modern.

Target Market(s)

Private clients, governments, corporations. Luxury and high market.

Industry/Entity Type

Health And Wellness

Contact Information for Business Card

Orlan Vitality should be the logo

Colors

Designer to choose colors to be used in the design.

Requirements
Must have
• Orlan Vitality
• Name: Dario Montalbe
• Wellness Coach, Consultant & Trainer.
• Website: www.orlanvitality-example.com
• Phone:
• Spain (+34) 612 480 597
• (USA) +1 (555) 318 0264
Nice to have
• The most important is the design of "Orlan Vitality", as this is going to be my personal brand logo. It should be professional, wellness, high end and actual.
Should not have
• no golds, no baroque style..

```html
<!DOCTYPE html>
<html lang="en">
<head>
<meta charset="utf-8">
<title>Orlan Vitality — Business Card</title>
<link rel="stylesheet" href="https://fonts.googleapis.com/css2?family=Oswald:wght@600&family=Arimo:ital,wght@0,400;0,700;1,700&display=swap">
<style>
  :root {
    --paper: #ffffff;
    --ink: #111311;
    --mist: #d6dcd8;
    --lime: #d8f70a;
    --leaf: #21a531;
    --contact: #545954;
  }
  html, body {
    margin: 0;
    padding: 0;
    width: 1200px;
    height: 720px;
    overflow: hidden;
    background: var(--paper);
  }
  .card {
    position: relative;
    width: 1200px;
    height: 720px;
    background: var(--paper);
    overflow: hidden;
  }
  .bar { position: absolute; }
  .bar--left-mist   { left: 37px;  top: 0;     width: 71px;  height: 461px; background: var(--mist); }
  .bar--left-leaf   { left: 37px;  top: 550px; width: 71px;  height: 170px; background: var(--leaf); }
  .bar--mid-mist    { left: 665px; top: 0;     width: 65px;  height: 257px; background: var(--mist); }
  .bar--mid-leaf    { left: 659px; top: 448px; width: 64px;  height: 272px; background: var(--leaf); }
  .bar--right-mist  { left: 844px; top: 0;     width: 39px;  height: 720px; background: var(--mist); }
  .bar--right-lime  { left: 883px; top: 0;     width: 154px; height: 720px; background: var(--lime); }
  .bar--right-leaf  { left: 1037px; top: 0;    width: 163px; height: 720px; background: var(--leaf); }

  .brand__name {
    position: absolute;
    left: 150px;
    top: 272px;
    margin: 0;
    font-family: "Arimo", Arial, sans-serif;
    font-weight: 700;
    font-size: 68px;
    line-height: 80px;
    color: var(--ink);
    white-space: nowrap;
  }
  .brand__tagline-box {
    position: absolute;
    left: 0;
    top: 390px;
    width: 760px;
    height: 56px;
  }
  .brand__tagline {
    font-family: "Oswald", Arial, sans-serif;
    font-weight: 600;
    fill: var(--ink);
  }

  .contact {
    position: absolute;
    left: 150px;
    top: 488px;
    font-family: "Arimo", Arial, sans-serif;
    color: var(--contact);
  }
  .contact__name {
    margin: 0 0 10px;
    font-size: 22px;
    font-weight: 700;
    font-style: italic;
  }
  .contact__line {
    margin: 0 0 11px;
    font-size: 23px;
    line-height: 27px;
  }
  .contact__line--phone-usa { margin-left: -4px; }
</style>
</head>
<body>
  <main class="card">
    <div class="bar bar--left-mist"></div>
    <div class="bar bar--left-leaf"></div>
    <div class="bar bar--mid-mist"></div>
    <div class="bar bar--mid-leaf"></div>
    <div class="bar bar--right-mist"></div>
    <div class="bar bar--right-lime"></div>
    <div class="bar bar--right-leaf"></div>

    <h1 class="brand__name">Orlan Vitality</h1>
    <svg class="brand__tagline-box" viewBox="0 0 760 56" aria-label="Wellness Coach. Consultant. Trainer.">
      <text class="brand__tagline" x="152" y="40" font-size="34" textLength="573" lengthAdjust="spacingAndGlyphs">WELLNESS COACH. CONSULTANT. TRAINER.</text>
    </svg>

    <section class="contact">
      <p class="contact__name">Dario Montalbe</p>
      <p class="contact__line">Spain (+34) 612 480 597</p>
      <p class="contact__line contact__line--phone-usa">(USA) +1 (555) 318 0264</p>
      <p class="contact__line">www.orlanvitality-example.com</p>
    </section>
  </main>
</body>
</html>
```